Letter and Envelope Design For Larchmont Realty

Please design a letter and an envelope incorporating our logo (See Attached). We are also launched a business card contest. Since we want them to match, please feel free to submit a design for both the business card and also the letter design and envelope.

Requirements
Must have
• The envelope, the letter and the business cards must match somehow connecting the designs. We want them to have something that holds them together besides the logo.

```html
<!DOCTYPE html>
<html lang="en">
<head>
<meta charset="utf-8">
<title>Larchmont Realty Stationery</title>
<link rel="stylesheet" href="https://fonts.googleapis.com/css2?family=Josefin+Sans:wght@600&family=Open+Sans:wght@600&display=swap">
<style>
  :root {
    --navy-light: #0a1f96;
    --navy-dark: #060f4a;
    --charcoal-light: #55575c;
    --charcoal-dark: #262628;
    --tab: #333336;
    --paper: #ffffff;
    --brand-blue: #0b1d8f;
    --stage: #ffffff;
  }
  html, body {
    margin: 0;
    padding: 0;
    width: 1200px;
    height: 879px;
    overflow: hidden;
    background: var(--stage);
  }
  .stationery-set { display: block; width: 1200px; height: 879px; }
  .paper { fill: var(--paper); }
  .tab { fill: var(--tab); }
  .white-rule { fill: var(--paper); }
  .navy-rule { fill: var(--brand-blue); }
  .brand-name {
    font-family: "Josefin Sans", sans-serif;
    font-weight: 600;
    text-anchor: middle;
  }
  .brand-name--light { fill: var(--paper); }
  .brand-name--blue { fill: var(--brand-blue); }
  .brand-ring--light { fill: none; stroke: var(--paper); }
  .brand-ring--blue { fill: none; stroke: var(--brand-blue); }
  .contact-line {
    font-family: "Open Sans", sans-serif;
    font-weight: 600;
    fill: var(--paper);
  }
  .contact-icon { fill: none; stroke: var(--paper); stroke-width: 0.8; }
</style>
</head>
<body>
<svg class="stationery-set" viewBox="0 0 1024 750" xmlns="http://www.w3.org/2000/svg">
  <defs>
    <linearGradient id="navy-fade" x1="0" y1="0" x2="1" y2="0">
      <stop offset="0" stop-color="var(--navy-light)"/>
      <stop offset="1" stop-color="var(--navy-dark)"/>
    </linearGradient>
    <linearGradient id="charcoal-fade" x1="0" y1="0" x2="1" y2="0">
      <stop offset="0" stop-color="var(--charcoal-light)"/>
      <stop offset="1" stop-color="var(--charcoal-dark)"/>
    </linearGradient>
    <filter id="sheet-shadow" x="-10%" y="-10%" width="120%" height="120%">
      <feDropShadow dx="0" dy="2" stdDeviation="3" flood-color="#000" flood-opacity="0.45"/>
    </filter>
  </defs>

  <!-- Letterhead -->
  <g class="letterhead" filter="url(#sheet-shadow)">
    <rect class="paper" x="601" y="56" width="401" height="630"/>
    <rect x="601" y="56" width="401" height="69" fill="url(#navy-fade)"/>
    <circle class="brand-ring--light" cx="801" cy="82" r="13" stroke-width="1.4"/>
    <text class="brand-name brand-name--light" x="801" y="105" font-size="7.5" letter-spacing="1">LARCHMONT</text>
    <text class="brand-name brand-name--light" x="801" y="113" font-size="5" letter-spacing="1.5">REALTY</text>
    <rect class="navy-rule" x="601" y="648" width="401" height="4"/>
    <rect x="601" y="652" width="401" height="34" fill="url(#charcoal-fade)"/>
    <polygon class="tab" points="742,648 748,638 854,638 860,648 860,686 742,686"/>
    <g class="contact-block">
      <path class="contact-icon" d="M781 645 q1 3 4 4"/>
      <text class="contact-line" x="788" y="649" font-size="6.5">+5550142</text>
      <circle class="contact-icon" cx="762" cy="657" r="1.6"/>
      <text class="contact-line" x="767" y="659" font-size="6.5">Elm Park Road 48. NC</text>
      <circle class="contact-icon" cx="762" cy="667" r="2.3"/>
      <text class="contact-line" x="767" y="669" font-size="6.5">larchmontrealty.com</text>
      <rect class="contact-icon" x="771" y="675" width="5" height="3.5"/>
      <text class="contact-line" x="779" y="679" font-size="6.5">lr_realty.com</text>
    </g>
  </g>

  <!-- Business card -->
  <g class="business-card" filter="url(#sheet-shadow)">
    <rect x="32" y="90" width="582" height="236" fill="url(#navy-fade)"/>
    <rect class="white-rule" x="32" y="326" width="582" height="6"/>
    <rect x="32" y="332" width="582" height="40" fill="url(#charcoal-fade)"/>
    <polygon class="tab" points="240,330 246,314 406,314 412,330 412,372 240,372"/>
    <circle class="brand-ring--light" cx="331" cy="164" r="48" stroke-width="5"/>
    <text class="brand-name brand-name--light" x="331" y="250" font-size="28" letter-spacing="3">LARCHMONT</text>
    <text class="brand-name brand-name--light" x="331" y="276" font-size="19" letter-spacing="5">REALTY</text>
    <g class="contact-block">
      <path class="contact-icon" d="M296 319 q1.5 4 5 5.5"/>
      <text class="contact-line" x="306" y="325" font-size="9">+5550142</text>
      <circle class="contact-icon" cx="271" cy="336" r="2.2"/>
      <text class="contact-line" x="278" y="340" font-size="9">Elm Park Road 48. NC</text>
      <circle class="contact-icon" cx="268" cy="350" r="3.2"/>
      <text class="contact-line" x="276" y="354" font-size="9">larchmontrealty.com</text>
      <rect class="contact-icon" x="284" y="362" width="7" height="5"/>
      <text class="contact-line" x="295" y="368" font-size="9">lr_realty.com</text>
    </g>
  </g>

  <!-- Envelope -->
  <g class="envelope" filter="url(#sheet-shadow)">
    <rect class="paper" x="32" y="385" width="582" height="283"/>
    <polygon points="32,385 614,385 582,467 74,467" fill="url(#navy-fade)"/>
    <circle class="brand-ring--blue" cx="322" cy="514" r="35" stroke-width="3.5"/>
    <text class="brand-name brand-name--blue" x="322" y="577" font-size="21" letter-spacing="2.5">LARCHMONT</text>
    <text class="brand-name brand-name--blue" x="322" y="596" font-size="14" letter-spacing="4">REALTY</text>
    <rect class="navy-rule" x="32" y="621" width="582" height="5"/>
    <rect x="32" y="626" width="582" height="42" fill="url(#charcoal-fade)"/>
    <polygon class="tab" points="238,625 246,608 404,608 412,625 412,668 238,668"/>
  </g>
</svg>
</body>
</html>
```